Need Business Card for our Indian Grocery Store

Industry/Entity Type

Grocery Store

Contact Information for Business Card

Manoj Baweja
Director

Store Locations:

Halden Vale
482 Elm Parade
P: 03 9172 5843

Marrick Hill
613 Carlow Road
P: 03 9238 6014

email: kvtmarts@mailnest.example

Requirements
Must have
• Our logo Colours

```html
<!DOCTYPE html>
<html lang="en">
<head>
<meta charset="utf-8">
<title>KVT Marts Business Card</title>
<link href="https://fonts.googleapis.com/css2?family=Libre+Caslon+Text:wght@400;700&family=Roboto:wght@400&display=swap" rel="stylesheet">
<style>
  :root {
    --brand-red: #e8151a;
    --brand-red-light: #fb3a3d;
    --brand-red-dark: #d30d10;
    --paper: #ffffff;
    --ink: #3a3a3a;
    --rule: #8a8a8a;
    --backdrop: #ece8e3;
  }
  html, body {
    margin: 0;
    padding: 0;
    width: 1200px;
    height: 1022px;
    overflow: hidden;
    background: var(--backdrop);
  }
  .canvas {
    position: relative;
    width: 1200px;
    height: 1022px;
  }
  .card {
    position: absolute;
    left: 350px;
    width: 512px;
    height: 300px;
    background: radial-gradient(ellipse at 55% 45%, var(--brand-red-light) 0%, var(--brand-red) 55%, var(--brand-red-dark) 100%);
    box-shadow: 0 6px 12px rgba(0,0,0,0.35);
    overflow: hidden;
  }
  .card--front { top: 192px; }
  .card--back { top: 516px; }
  .card__frame {
    position: absolute;
    inset: 0;
    width: 512px;
    height: 300px;
  }
  .front-name {
    position: absolute;
    left: 0;
    right: 0;
    top: 100px;
    text-align: center;
    font-family: "Libre Caslon Text", serif;
    font-weight: 400;
    font-size: 90px;
    line-height: 1;
    color: var(--paper);
  }
  .brand-name {
    position: absolute;
    left: 50px;
    width: 214px;
    top: 136px;
    text-align: center;
    white-space: nowrap;
    font-family: "Libre Caslon Text", serif;
    font-weight: 700;
    font-size: 34px;
    line-height: 1;
    color: var(--brand-red);
  }
  .divider {
    position: absolute;
    left: 274px;
    top: 102px;
    width: 1px;
    height: 112px;
    background: var(--rule);
  }
  .contact {
    position: absolute;
    left: 294px;
    top: 60px;
    color: var(--ink);
  }
  .contact__name {
    font-family: "Libre Caslon Text", serif;
    font-weight: 700;
    font-size: 20px;
    line-height: 22px;
  }
  .contact__role {
    font-family: "Libre Caslon Text", serif;
    font-size: 16px;
    line-height: 20px;
    margin-bottom: 12px;
  }
  .contact__list {
    list-style: none;
    margin: 0;
    padding: 0;
    font-family: "Roboto", sans-serif;
    font-size: 11px;
    line-height: 18.7px;
  }
  .contact__item {
    display: flex;
    align-items: center;
    gap: 6px;
    white-space: nowrap;
  }
  .contact__item--indent { padding-left: 23px; }
  .icon { width: 16px; height: 14px; flex: none; }
</style>
</head>
<body>
<div class="canvas">

  <section class="card card--front" aria-label="Card front">
    <svg class="card__frame" viewBox="0 0 512 300" aria-hidden="true">
      <path d="M3 45 Q3 26 22 24 Q256 -6 490 24 Q509 26 509 45 L509 250 Q509 268 490 271 Q256 305 22 271 Q3 268 3 250 Z"
            fill="none" stroke="#ffffff" stroke-width="4"/>
    </svg>
    <div class="front-name">KVT</div>
  </section>

  <section class="card card--back" aria-label="Card back">
    <svg class="card__frame" viewBox="0 0 512 300" aria-hidden="true">
      <path d="M3 55 Q3 36 22 33 Q256 -4 490 33 Q509 36 509 55 L509 240 Q509 258 490 261 Q256 302 22 261 Q3 258 3 240 Z"
            fill="none" stroke="#ffffff" stroke-width="3"/>
      <path d="M6 60 Q6 44 22 42 Q256 8 490 42 Q506 44 506 60 L506 236 Q506 252 490 254 Q256 290 22 254 Q6 252 6 236 Z"
            fill="#ffffff"/>
    </svg>

    <div class="brand-name">KVT Marts</div>

    <div class="divider"></div>

    <div class="contact">
      <div class="contact__name">Manoj Baweja</div>
      <div class="contact__role">Director</div>
      <ul class="contact__list">
        <li class="contact__item">
          <svg class="icon" viewBox="0 0 16 14" aria-hidden="true"><path d="M8 1 L15 7 H13 V13 H9.5 V9 H6.5 V13 H3 V7 H1 Z" fill="var(--brand-red)"/></svg>
          Halden Vale
        </li>
        <li class="contact__item contact__item--indent">482 Elm Parade</li>
        <li class="contact__item">
          <svg class="icon" viewBox="0 0 16 14" aria-hidden="true"><path d="M2 5 Q8 0 14 5 L12 6 Q8 3 4 6 Z" fill="var(--brand-red)"/><rect x="4" y="6" width="8" height="7" rx="1" fill="var(--brand-red)"/><circle cx="8" cy="9.5" r="1.8" fill="#fff"/></svg>
          03 9172 5843
        </li>
        <li class="contact__item">
          <svg class="icon" viewBox="0 0 16 14" aria-hidden="true"><path d="M8 1 L15 7 H13 V13 H9.5 V9 H6.5 V13 H3 V7 H1 Z" fill="var(--brand-red)"/></svg>
          Marrick Hill
        </li>
        <li class="contact__item contact__item--indent">613 Carlow Road</li>
        <li class="contact__item">
          <svg class="icon" viewBox="0 0 16 14" aria-hidden="true"><path d="M2 5 Q8 0 14 5 L12 6 Q8 3 4 6 Z" fill="var(--brand-red)"/><rect x="4" y="6" width="8" height="7" rx="1" fill="var(--brand-red)"/><circle cx="8" cy="9.5" r="1.8" fill="#fff"/></svg>
          03 9238 6014
        </li>
        <li class="contact__item">
          <svg class="icon" viewBox="0 0 16 14" aria-hidden="true"><rect x="1.5" y="2.5" width="13" height="9" fill="none" stroke="var(--brand-red)" stroke-width="1.3"/><path d="M1.5 2.5 L8 8 L14.5 2.5" fill="none" stroke="var(--brand-red)" stroke-width="1.3"/></svg>
          kvtmarts@mailnest.example
        </li>
      </ul>
    </div>
  </section>

</div>
</body>
</html>
```